Contractor Business Card Design

Looking to have a card made that has a bold description of (KITCHENS, BASEMENTS, BATHROOMS)

Definition and layers a plus

Contact info is;

Mark T. Ellery
Millbrook, MN 55012
Cell: 612-555-0147
website: www.cobaltfinishworks.example
Email: cobaltfinishworksmn@mailbox.example

colors: red, black, gray, white

Contact Information for Business Card

Contact info is;

Mark T. Ellery
Millbrook, MN 55012
Cell: 612-555-0147

Colors
ec1f27

Requirements
Must have
• Looking for layers and definition
Nice to have
• Cards are planned to be printed on plastic cards

```html
<!DOCTYPE html>
<html lang="en">
<head>
<meta charset="utf-8">
<title>Cobalt Finish Works – Business Card</title>
<link rel="stylesheet" href="https://fonts.googleapis.com/css2?family=Roboto:wght@400;700;900&display=swap">
<style>
  :root {
    --brand-red: #ec1f27;
    --ink: #1a1a1a;
    --stone: #d3d3d3;
    --stone-dark: #b4b4b4;
    --blush: #f2a3a6;
    --blush-dark: #e58a8e;
    --muted: #c8c8c8;
    --rule: #f6c6c8;
    --paper: #ffffff;
    --backdrop: #c9c9c9;
  }
  * { margin: 0; padding: 0; box-sizing: border-box; }
  html, body {
    width: 1167px; height: 1200px; overflow: hidden;
    background: var(--backdrop);
    font-family: "Roboto", Arial, sans-serif;
  }
  .card {
    position: absolute; left: 58px; top: 300px;
    width: 1050px; height: 600px;
    background: var(--paper);
    box-shadow: 0 6px 18px rgba(0,0,0,0.18);
  }
  .brand {
    position: absolute; left: 60px; top: 55px; width: 350px;
    display: flex; flex-direction: column; align-items: center;
  }
  .brand-ring {
    width: 150px; height: 150px; border-radius: 50%;
    border: 6px solid var(--ink);
  }
  .brand-name {
    margin-top: 22px; text-align: center;
    font-weight: 700; font-size: 38px; line-height: 1.1;
    letter-spacing: 3px; color: var(--ink);
  }
  .services {
    position: absolute; left: 60px; top: 385px;
    font-weight: 900; font-size: 50px; line-height: 56px;
    letter-spacing: 3px; color: var(--stone);
    text-shadow: 2px 2px 0 var(--stone-dark);
  }
  .services li { list-style: none; }
  .services li:nth-child(2) { padding-left: 18px; }
  .services li:nth-child(3) { padding-left: 36px; }
  .services .accent { color: var(--blush); text-shadow: 2px 2px 0 var(--blush-dark); }
  .contact { position: absolute; left: 560px; top: 165px; width: 440px; }
  .phone-row { display: flex; align-items: center; gap: 12px; }
  .icon {
    flex: none; border-radius: 50%; background: var(--brand-red);
    display: flex; align-items: center; justify-content: center;
  }
  .icon svg { display: block; }
  .phone-row .icon { width: 44px; height: 44px; }
  .phone-number {
    font-weight: 700; font-size: 48px; line-height: 1; color: var(--brand-red);
    letter-spacing: 1px;
  }
  .name-line {
    display: flex; justify-content: space-between; align-items: flex-end;
    width: 420px; margin-top: 4px;
  }
  .address { padding-left: 10px; font-size: 13px; color: var(--muted); }
  .person { padding-right: 40px; font-weight: 700; font-size: 26px; line-height: 1; color: var(--ink); }
  .rule { margin-top: 10px; height: 7px; width: 420px; background: var(--rule); }
  .links { margin-top: 95px; padding-left: 30px; }
  .link-row { display: flex; align-items: center; gap: 14px; margin-bottom: 14px; }
  .link-row .icon { width: 30px; height: 30px; }
  .web { font-size: 24px; color: var(--brand-red); }
  .mail { font-size: 19px; color: var(--brand-red); }
</style>
</head>
<body>
  <article class="card">
    <div class="brand">
      <div class="brand-ring"></div>
      <div class="brand-name">COBALT FINISH<br>WORKS</div>
    </div>

    <ul class="services">
      <li>KITCHEN<span class="accent">S</span></li>
      <li>BASEMENT<span class="accent">S</span></li>
      <li>BATHROOM<span class="accent">S</span></li>
    </ul>

    <section class="contact">
      <div class="phone-row">
        <span class="icon">
          <svg width="24" height="24" viewBox="0 0 24 24" fill="none" stroke="#fff" stroke-width="2" stroke-linejoin="round">
            <path d="M5 3h4l2 5-2.5 1.5a11 11 0 0 0 6 6L16 13l5 2v4a2 2 0 0 1-2 2A16 16 0 0 1 3 5a2 2 0 0 1 2-2z"/>
          </svg>
        </span>
        <span class="phone-number">612-555-0147</span>
      </div>
      <div class="name-line">
        <span class="address">Millbrook, MN 55012</span>
        <span class="person">Mark T. Ellery</span>
      </div>
      <div class="rule"></div>

      <div class="links">
        <div class="link-row">
          <span class="icon">
            <svg width="20" height="20" viewBox="0 0 24 24" fill="none" stroke="#fff" stroke-width="1.8">
              <circle cx="12" cy="12" r="9"/>
              <ellipse cx="12" cy="12" rx="4" ry="9"/>
              <path d="M3 12h18M5 7h14M5 17h14"/>
            </svg>
          </span>
          <span class="web">www.cobaltfinishworks.example</span>
        </div>
        <div class="link-row">
          <span class="icon">
            <svg width="18" height="18" viewBox="0 0 24 24" fill="none" stroke="#fff" stroke-width="2" stroke-linejoin="round">
              <rect x="3" y="6" width="18" height="12"/>
              <path d="M3 6l9 7 9-7"/>
            </svg>
          </span>
          <span class="mail">cobaltfinishworksmn@mailbox.example</span>
        </div>
      </div>
    </section>
  </article>
</body>
</html>
```